Business Card Design

building company specialistloft conversion,extension ,bathrooms ,kitchens ,painting and decorating all general building work

Industry/Entity Type

Building

Contact Information for Business Card

K&M Property renovation Ltd
tel -07914638205
email-Mdorin07@brixmail.net
web in progres

Font styles to use
Sans Serif

Requirements
Must have
• name of the company
• all contact details
Nice to have
• some of the skills

```html
<!DOCTYPE html>
<html lang="en">
<head>
<meta charset="utf-8">
<title>K&amp;M Property Renovation Ltd – Business Card</title>
<link rel="stylesheet" href="https://fonts.googleapis.com/css2?family=Open+Sans:wght@400;600&display=swap">
<style>
  :root {
    --backdrop: #2b2624;
    --card: #141414;
    --card-edge: #1f1f1f;
    --orange: #f39419;
    --white: #f2f2f2;
    --grey: #b9b9b9;
    --silver: #c9c9c9;
    --divider: #3a3a3a;
  }
  * { margin: 0; padding: 0; box-sizing: border-box; }
  html, body {
    width: 1200px; height: 844px; overflow: hidden;
    background: var(--backdrop);
    font-family: "Open Sans", sans-serif;
  }
  .stage {
    width: 1200px; height: 844px;
    display: flex; align-items: center; justify-content: center; gap: 60px;
  }
  .card {
    width: 520px; height: 300px;
    background: var(--card);
    border: 1px solid var(--card-edge);
    border-radius: 4px;
    position: relative;
    box-shadow: 0 12px 30px rgba(0,0,0,.45);
  }
  .brand {
    position: absolute; left: 40px; top: 48px;
    display: flex; align-items: center; gap: 14px;
  }
  .brand-dot {
    width: 14px; height: 14px; border-radius: 50%;
    background: var(--orange); flex: none;
  }
  .brand-name {
    font-weight: 600; font-size: 24px; color: var(--orange);
    letter-spacing: .5px; white-space: nowrap;
  }
  .person {
    position: absolute; left: 40px; top: 150px; width: 210px;
  }
  .person-name { font-size: 20px; font-weight: 600; color: var(--orange); line-height: 1.2; }
  .person-role { font-size: 14px; color: var(--grey); margin-bottom: 14px; }
  .address { font-size: 14px; color: var(--white); line-height: 1.35; }
  .divider {
    position: absolute; left: 262px; top: 150px;
    width: 1px; height: 110px; background: var(--divider);
  }
  .contacts {
    position: absolute; left: 282px; top: 150px;
    list-style: none;
  }
  .contacts li {
    display: flex; align-items: center; gap: 9px;
    font-size: 14px; color: var(--white); height: 26px; white-space: nowrap;
  }
  .icon {
    width: 16px; height: 16px; border-radius: 2px;
    background: var(--orange);
    display: flex; align-items: center; justify-content: center; flex: none;
  }
  .icon svg { width: 10px; height: 10px; }
  .back-brand {
    position: absolute; inset: 0;
    display: flex; align-items: center; justify-content: center; gap: 14px;
  }
  .back-brand .brand-dot { background: var(--silver); }
  .back-brand .brand-name { color: var(--silver); font-size: 26px; }
</style>
</head>
<body>
<main class="stage">
  <section class="card card-front" aria-label="Business card front">
    <div class="brand">
      <span class="brand-dot"></span>
      <span class="brand-name">K&amp;M Property Renovation Ltd</span>
    </div>

    <div class="person">
      <p class="person-name">Daniel Reeve</p>
      <p class="person-role">Managing Director</p>
      <p class="address">12345, Address Goes Here<br>Country Name, 123456</p>
    </div>

    <div class="divider"></div>

    <ul class="contacts">
      <li>
        <span class="icon"><svg viewBox="0 0 10 10"><path d="M2 1 L4 1 L4.6 3 L3.4 4 Q4.5 6 6 6.6 L7 5.4 L9 6 L9 8 Q8.5 9 7.5 9 Q1 8 1 2.5 Q1 1.5 2 1Z" fill="#fff"/></svg></span>
        (044)-456-7890
      </li>
      <li>
        <span class="icon"><svg viewBox="0 0 10 10"><rect x="2.5" y="0.8" width="5" height="8.4" rx="1" fill="#fff"/><rect x="3.4" y="2" width="3.2" height="5" fill="#f39419"/></svg></span>
        123-456-7890
      </li>
      <li>
        <span class="icon"><svg viewBox="0 0 10 10"><rect x="1" y="2.3" width="8" height="5.4" fill="#fff"/><path d="M1 2.3 L5 5.5 L9 2.3" stroke="#f39419" stroke-width="0.8" fill="none"/></svg></span>
        info@youremail.com
      </li>
      <li>
        <span class="icon"><svg viewBox="0 0 10 10"><path d="M4 6 L6 4 M3.5 4.5 L2.3 5.7 A1.5 1.5 0 0 0 4.3 7.7 L5.5 6.5 M6.5 5.5 L7.7 4.3 A1.5 1.5 0 0 0 5.7 2.3 L4.5 3.5" stroke="#fff" stroke-width="1.1" fill="none" stroke-linecap="round"/></svg></span>
        www.website.com
      </li>
    </ul>
  </section>

  <section class="card card-back" aria-label="Business card back">
    <div class="back-brand">
      <span class="brand-dot"></span>
      <span class="brand-name">K&amp;M Property Renovation Ltd</span>
    </div>
  </section>
</main>
</body>
</html>
```